Simple psychologist website
Open brief, creative designs encouraged
Site map:
Home
our services
our psychologists
selective mutism
resources
contact

Current website:
http://mindsproutyouth.com.au/
Not in love with our logo, or colours etc - open brief
Happy for new font/style/logo for company name - if we choose a logo design from a designer who doesn't win the competition, we will award $50 for the logo and use it in the new website

Website made a few years ago for a sister company that we really like:
http://www.korrelpsychology.com.au/

Clean, credible and warm and friendly look & feel
stock photos OK, designer will be required to hand over any images used in the design as shown in the PSD

Target Market(s)

Adolescents with psychological issues and their families

Industry/Entity Type

Psychology

Number of Pages Required

2 page

Colors

Designer to choose colors to be used in the design.

Requirements
Must have
• One home page - simple with 2 or 3 small areas to tease and attract the user and one template page to suit all the other pages
• We like slides, we want to have 3 slides like korrelpsychology.com.au
• Three slide titles:
• 1. We specialise in many areas, find the right clinical psychologist for your family
• 2. Child Clinical Psychologists in Chatswood and Westmead
• 3. Resources
• Pages structurally similar to
• http://www.korrelpsychology.com.au/
• We like the 'featured' items, which in our case will have splash box titles (can be 3 or 4):
• 1. Selective Mutism
• 2. Is my child anxious?
• 3. Does my child have an eating disorder?
• 4. Parenting adolescents
• Does not need to be a copy of http://www.korrelpsychology.com.au/ and we are willing to accept outside-the-box thinking and design (we in fact encourage it)
• Owner of business wants to highlight Selective Mutism as they have specialists. Consider ways that may make this work.
• Design winner will be based on home page design but winning designer will be required to provide an additional but simpler 'standard' page template design based on the themes used in the winning design.

```html
<!DOCTYPE html>
<html lang="en">
<head>
<meta charset="utf-8">
<title>Kindlewood – Child, Adolescent &amp; Family Psychology</title>
<link rel="stylesheet" href="https://fonts.googleapis.com/css2?family=Courgette&family=Montserrat:wght@400;600;700&family=Open+Sans:wght@400;600;700&display=swap">
<style>
:root{
  --blue:#27a4dd;
  --blue-dark:#1d86c6;
  --ink:#333a44;
  --grey:#6b6f75;
  --grey-light:#9a9ea4;
  --line:#d7dbe0;
  --slate:#5b5d60;
  --footer:#2c303b;
  --footer-deep:#22252e;
  --footer-text:#a7abb4;
  --pale:#eef2f6;
  --white:#ffffff;
}
*{box-sizing:border-box;margin:0;padding:0}
html,body{width:1200px;height:2503px;overflow:hidden;background:var(--white)}
body{position:relative;font-family:"Open Sans",Arial,sans-serif;color:var(--ink)}
.abs{position:absolute}

/* header */
.brand{left:87px;top:40px;display:flex;align-items:center;gap:14px}
.brand-mark{width:22px;height:22px;border-radius:50%;background:var(--blue)}
.brand-name{font-family:"Open Sans",Arial,sans-serif;font-weight:700;font-size:38px;color:var(--blue);line-height:1}
.brand-tag{left:123px;top:88px;font-family:"Open Sans",Arial,sans-serif;font-weight:600;font-size:15px;color:var(--ink)}
.pill{top:63px;height:54px;border-radius:27px;background:linear-gradient(#fff,#eceef0);box-shadow:0 3px 6px rgba(0,0,0,.12);display:flex;align-items:center;padding-left:26px;gap:10px}
.pill small{position:absolute;top:-2px;left:56px;font-size:14px;color:var(--ink)}
.pill strong{font-family:"Montserrat",Arial,sans-serif;font-size:20px;font-weight:600;color:var(--ink);padding-top:10px}
.pill svg{margin-top:10px}
.pill-phone{left:638px;width:213px}
.pill-mail{left:865px;width:240px}
.header-rule{left:0;top:154px;width:1200px;height:3px;background:var(--blue-dark)}
.main-nav{top:171px;left:0;width:1200px;display:flex;justify-content:center;gap:38px;font-family:"Montserrat",Arial,sans-serif;font-weight:700;font-size:13px;letter-spacing:.3px}
.main-nav a{color:var(--ink);text-decoration:none}
.main-nav a.active{color:var(--blue)}

/* hero */
.hero{left:87px;top:210px;width:1028px;height:439px;overflow:hidden;background:linear-gradient(90deg,#f4f6f7 0%,#f0f1ee 30%,#d9c9bc 55%,#c9b3a2 75%,#9fb67f 100%)}
.hero-photo{left:0;top:0;width:1028px;height:439px}
.hero-circle{left:5px;top:17px;width:400px;height:400px;border-radius:50%;background:var(--blue);padding:108px 44px 0 60px;color:var(--white)}
.hero-circle h1{font-family:"Courgette",cursive;font-weight:400;font-size:24px;line-height:41px;margin-bottom:8px}
.hero-circle p{font-size:14px;line-height:22px}
.more-btn{left:282px;top:294px;width:118px;height:118px;border-radius:50%;background:var(--slate);border:3px dotted rgba(255,255,255,.8);outline:4px solid var(--slate);display:flex;align-items:center;justify-content:center;text-align:center;font-family:"Montserrat",Arial,sans-serif;font-weight:600;font-size:16px;color:var(--white);line-height:22px}

/* who we are */
.section-title{left:0;width:1200px;text-align:center;font-family:"Courgette",cursive;font-weight:400;font-size:44px;color:var(--ink)}
.intro{left:100px;top:810px;width:970px;text-align:center;font-size:13.5px;line-height:24px;color:var(--grey)}
.feature{font-size:13px;line-height:21px;color:var(--grey)}
.feature h3{font-family:"Montserrat",Arial,sans-serif;font-weight:700;font-size:16px;color:var(--ink);margin-bottom:4px;letter-spacing:.2px}
.feature.left{text-align:right}
.focus-brand{left:481px;top:1090px;width:200px;text-align:center}
.focus-brand .brand-name{font-size:34px}
.focus-brand span{display:block;font-weight:600;font-size:15px;line-height:19px;color:var(--ink);margin-top:6px}

/* advice */
.advice{left:0;top:1302px;width:1200px;height:611px;background:linear-gradient(90deg,#c9d4da 0%,#dfe5ea 30%,#eef2f5 50%,var(--pale) 100%)}
.advice-photo{left:0;top:0;width:560px;height:611px;background:linear-gradient(90deg,#4c86c0 0%,#9cb7cf 35%,#e7ecef 75%,rgba(238,242,246,0) 100%)}
.advice h2{left:601px;top:78px;font-family:"Montserrat",Arial,sans-serif;font-weight:700;font-size:38px;color:var(--ink)}
.advice .sub{left:604px;top:143px;font-size:16px;color:var(--grey)}
.field{background:var(--white);border:1px solid var(--line);border-radius:2px;font-size:12px;color:var(--grey-light);padding:12px 16px}
.send-btn{left:601px;top:425px;width:128px;height:32px;background:var(--blue);color:var(--white);font-family:"Montserrat",Arial,sans-serif;font-weight:700;font-size:9px;display:flex;align-items:center;justify-content:center;border-radius:2px}

/* map */
.map{left:0;top:1913px;width:1200px;height:257px;background:linear-gradient(180deg,#eceeef,#e3e6e8)}

/* footer */
.footer{left:0;top:2170px;width:1200px;height:295px;background:var(--footer);font-family:"Montserrat",Arial,sans-serif}
.footer h4{position:absolute;top:52px;font-weight:700;font-size:17px;color:var(--white);letter-spacing:-.2px}
.footer ul{position:absolute;top:80px;list-style:none;font-size:11px;line-height:28.4px;color:var(--footer-text)}
.news-sub{position:absolute;left:479px;top:80px;font-size:12px;color:var(--footer-text)}
.news-input{position:absolute;left:479px;top:113px;width:259px;height:37px;background:var(--footer-deep);border-radius:2px;font-size:12px;color:#7e838c;padding:11px 14px}
.socials{position:absolute;left:483px;top:170px;display:flex;gap:14px}
.socials span{width:12px;height:12px;border-radius:50%;background:#6f7f9b}
.subscribe{position:absolute;left:481px;top:203px;width:133px;height:35px;background:var(--blue);color:var(--white);font-weight:700;font-size:13px;display:flex;align-items:center;justify-content:center}
.contact-list{position:absolute;left:876px;top:82px;font-size:11px;color:var(--footer-text)}
.contact-list div{display:flex;line-height:26px}
.contact-list b{color:var(--white);width:58px;font-weight:700}
.contact-list i{font-style:normal;width:11px;color:var(--white)}
.copyright{left:0;top:2465px;width:1200px;height:38px;background:var(--footer-deep);color:var(--footer-text);font-family:"Montserrat",Arial,sans-serif;font-size:12px;display:flex;align-items:center;justify-content:center}
</style>
</head>
<body>

<header>
  <div class="abs brand"><span class="brand-mark"></span><span class="brand-name">Kindlewood</span></div>
  <div class="abs brand-tag">Child, Adolescent &amp; Family Psychology</div>

  <div class="abs pill pill-phone">
    <small>(Call us)</small>
    <svg width="18" height="16" viewBox="0 0 18 16"><path d="M2 5c0-3 14-3 14 0v2h-4V5H6v2H2z M5 8h8l3 7H2z" fill="#555"/></svg>
    <strong>+1800-555-0142</strong>
  </div>
  <div class="abs pill pill-mail">
    <small>(E-mail)</small>
    <svg width="16" height="16" viewBox="0 0 16 16"><rect x="1" y="3" width="14" height="11" fill="#555"/><path d="M1 3l7 6 7-6" stroke="#fff" stroke-width="1.3" fill="none"/></svg>
    <strong style="font-size:17px">hello@kindlewoodpsych.com</strong>
  </div>
  <div class="abs header-rule"></div>
  <nav class="abs main-nav">
    <a class="active" href="#">HOME</a>
    <a href="#">OUR SERVICES</a>
    <a href="#">OUR PSYCHOLOGISTS</a>
    <a href="#">SELECTIVE MUTISM</a>
    <a href="#">RESOURCES</a>
    <a href="#">CONTACT</a>
  </nav>
</header>

<section class="abs hero">
  <div class="abs hero-photo" role="img" aria-label="Photo of a smiling family: parents carrying two children piggyback outdoors"></div>
  <div class="abs hero-circle">
    <h1>Child Clinical Psychologists in Chatswood &amp; Westmead</h1>
    <p>Lorem Ipsum has been the industry's standard dummy text ever since the 1500s, when an unknown printer took a galley of type and scrambled it to make a type specimen book.</p>
  </div>
  <div class="abs more-btn">MORE<br>DETAILS</div>
</section>

<section>
  <h2 class="abs section-title" style="top:722px">Who We Are</h2>
  <p class="abs intro">Lorem Ipsum has been the industry's standard dummy text ever since the 1500s, when an unknown printer took a galley of type and scrambled it to make a type specimen book. It has survived not only five centuries, but also the leap into electronic typesetting, remaining essentially unchanged. It was popularised in the 1960s with the release of Letraset sheets containing Lorem Ipsum passages,</p>

  <svg class="abs" style="left:340px;top:970px" width="482" height="250" viewBox="0 0 482 250">
    <path d="M13 236 A228 228 0 0 1 469 236" fill="none" stroke="var(--blue-dark)" stroke-width="2.5"/>
    <line x1="13" y1="236" x2="13" y2="236" stroke="var(--blue-dark)"/>
    <circle cx="13" cy="236" r="4" fill="var(--blue-dark)"/>
    <circle cx="469" cy="236" r="4" fill="var(--blue-dark)"/>
    <circle cx="26" cy="156" r="7" fill="var(--blue-dark)"/>
    <circle cx="127" cy="36" r="7" fill="var(--blue-dark)"/>
    <circle cx="355" cy="36" r="7" fill="var(--blue-dark)"/>
    <circle cx="456" cy="156" r="7" fill="var(--blue-dark)"/>
  </svg>

  <div class="abs feature left" style="left:140px;top:982px;width:257px">
    <h3>SELECTIVE MUTISM</h3>Solution for families that need<br>an extra level of care
  </div>
  <div class="abs feature left" style="left:80px;top:1100px;width:242px">
    <h3>IS MY CHILD ANXIOUS?</h3>From companionship services<br>to hospice care support
  </div>
  <div class="abs feature" style="left:781px;top:972px;width:260px">
    <h3>DOES MY CHILD HAVE AN EATING DISORDER?</h3>We provide transportation services<br>you can rely on
  </div>
  <div class="abs feature" style="left:841px;top:1100px;width:260px">
    <h3>PARENTING ADOLESCENTS</h3>We are looking for caring individuals<br>to join our teams
  </div>

  <div class="abs focus-brand">
    <span class="brand-name">Kindlewood</span>
    <span>Child,<br>Adolescent &amp;<br>Family Psychology</span>
  </div>
</section>

<section class="abs advice">
  <div class="abs advice-photo" role="img" aria-label="Photo of a nurse embracing a smiling older woman"></div>
  <h2 class="abs">Looking for Advice ?</h2>
  <p class="abs sub">Your request will be answered withing 24 hours</p>
  <div class="abs field" style="left:601px;top:195px;width:237px;height:42px">Name *</div>
  <div class="abs field" style="left:850px;top:195px;width:238px;height:42px">E-mail *</div>
  <div class="abs field" style="left:601px;top:254px;width:487px;height:143px">Message</div>
  <div class="abs send-btn">SEND MESSAGE</div>
</section>

<div class="abs map" role="img" aria-label="Street map showing the clinic location"></div>
<svg class="abs" style="left:518px;top:2001px" width="28" height="40" viewBox="0 0 28 40"><path d="M14 0C6 0 0 6 0 14c0 10 14 26 14 26s14-16 14-26C28 6 22 0 14 0z" fill="var(--blue)"/><circle cx="14" cy="14" r="5" fill="#fff"/></svg>

<footer class="abs footer">
  <h4 style="left:123px">Quick Links</h4>
  <ul style="left:123px"><li>HOME</li><li>ABOUT US</li><li>SERVICES</li><li>DOCTORS</li><li>TESTIMONIAL</li><li>BOOK APPOINTMENT</li></ul>
  <ul style="left:297px"><li>DEPARTMENTS</li><li>FAQ</li><li>NEWS</li><li>BLOG</li><li>CONTACT US</li><li>CAREERS</li></ul>

  <h4 style="left:479px;top:46px;font-size:15px">NEWSLETTER</h4>
  <div class="news-sub">SUBSCRIBE YOUR NEWSLETTER</div>
  <div class="news-input">Email Address</div>
  <div class="socials"><span></span><span></span><span></span><span></span></div>
  <div class="subscribe">SUBSCRIBE</div>

  <h4 style="left:876px">Contact Us</h4>
  <div class="contact-list">
    <div><b>ADDRESS</b><i>:</i><span>HARBOURVIEW CLINIC<br>ALDER LANE STREET<br>NSW 2067</span></div>
    <div style="margin-top:4px"><b>EMAIL</b><i>:</i><span>CARE@HARBOURVIEWCLINIC.COM</span></div>
    <div style="margin-top:4px"><b>PHONE</b><i>:</i><span>0291 5550 172</span></div>
  </div>
</footer>
<div class="abs copyright">COPYRIGHT 2016 © KINDLEWOOD. ALLRIGHT RESERVED</div>

</body>
</html>
```